Lantern Cafe - Menu Redesign

What We Want

We're looking for a bold redesign of our current menu. Our current menu is tired and boring and does not accurately reflect our revitalization of the Lantern Cafe brand. Attachments will be submitted with the campaign for menu items.

Design Guidelines

• Creative use of typography and color. Think Bold, Fun, Loud and uninhibited.
• Fluid, easy to read, layout that emphasizes readability.
• The subtle, demure, look of typographic columns (examples below in resources)
• Creative use of 'wells' for menu item highlights as well as great boarders
• Loud typefaces as long as readability is the focus & emphasis.
• Small illustrations/icons but they must not effect or take the focus from the readability of the menu
• Big, oversized, menu that will look great on recycled paper
• Subtle watermarks/illustrations
• creative use of textures / highlights / section breaks

Menu Requirements

• 9”x12” paper size. Please notify us if your design works better in a different format.
• Oversized, designed for printing on recycled paper.
• Single Page Menu (use lunch on front and breakfast on back)
• Do not use $ or "..." in pricing. Please space all prices equally.
• Simplistic layout that emphasizes readability and logical navigation of menu items.
• Acceptable file types
• Photoshop
• Indesign
• illustrator
• Please contact us before you submit a design if you plan on using something else
• HTML/CSS would be a huge benefit. It's not a must, but it will definitely help you win the award.
• Must retain some of our current color scheme (red/orange/yellow – see attachments/website).

NOTE: Please download ALL attached resources for the project.

Current web site:  www.lanterncafe-example.com

please read attachment:  lantern_menu_redesign_request.docx

Lots of good information & examples on menus we like and the design elements featured in the menu.

All,

Thanks for your design submissions!  With all the designs that have be submitted so far, we are confident that our money will be well spent.  I have changed the project to non-refundable.  Please continue working on your designs using the design_request doc that's posted for guidelines/requirements.  I will provide specific feedback to designs as needed.

For your convenience:

Design Guidelines

 

Creativeuse of typography and color.  Think Bold,Fun, Loud and uninhibited.

Fluid,easy to read, layout that emphasizes readability.

Thesubtle, demure, look of typographic columns (examples below in resources)

Creativeuse of 'wells' for menu item highlights as well as great boarders

Loudtypefaces as long as readability is the focus & emphasis.

Smallillustrations/icons but they must not effect or take the focus from thereadability of the menu

Big,oversized, menu that will look great on recycled paper

Subtlewatermarks/illustrations

creativeuse of textures / highlights / section breaks

 

  MenuRequirements

 

9”x12”paper size.  Please notify us if yourdesign works better in a different format.

Oversized,designed for printing on recycled paper.

SinglePage Menu (use lunch on front and breakfast on back)

Donot use $ or "..." in pricing.Please space all prices equally.

Simplisticlayout that emphasizes readability and logical navigation of menu items.

Acceptablefile types

Photoshop

Indesign

illustrator 

Pleasecontact us before you submit a design if you plan on using something else

HTML/CSSwould be a huge benefit.  It's not amust, but it will definitely help you win the award.

Mustretain some of our current color scheme (red/orange/yellow – seeattachments/website). 

 

Do Not Use

 

Skeuomorphismin any way.

Wedo not want any actual pictures of food on the menu (subtle illustrations /icons are great and encouraged).

Typefacesthat are hard to read.

Thanks!

dale

Please expect some new copy tonight (USA EST) for the breakfast menu items.  Thanks!

dale

COPY UPDATE:  Please check new menu item listing (revision 3) for updated copy.  Please revisit all menu items as I have grouped, consolidated, and eliminated some items.

Thanks!

dale 

DESIGN UPDATE:  I added an omelette hero/jumbotron design that we'd like to use to display the omelettes on the breakfast menu.  It doesn't have to be exactly like this one, it's just meant to be a guideline.  Please take a look and see if you can fit it in to your design.  Also, the copy has been updated for the breakfast & lunch menus.

Reason: Designer needs more tine to complete final submission. This will be the last extension. Thanks! dale

Target Market(s)

Women - 60% or more. Mostly professionals. 18-55.
Men - Professionals mostly. Judges, Attorneys, Agents, Ect. Ages 18-55.

Industry/Entity Type

Printing

Colors
f37022
ec1f27
f78f20
faa54b
f04a50
fee18a
faee3e

Requirements
Must have
• see menu requirements in task description.
Nice to have
• Design Ideas We Love

http://www.plateglimpse-example.com/menuwall/archives/oakbarrel_inn.php
We like: typefaces, typographic columns & layout, use of butcher-block print, simplicity
We don't like: lack of bold, color lack of textures, lack of general vitality in the brand, no use of icons/illustrations

http://www.plateglimpse-example.com/menuwall/archives/grillhaven_pub.php
We like: typefaces, bold headers & section breaks, texturized typefaces, use of illustrations, and specifically we love how they did the 'custom creation' menu
We don't like: lack of bold color, lack of subtle texturing, little more use of illustrated icons would be nice

http://www.plateglimpse-example.com/menuwall/archives/the_humming_goose.php
We like: use of bold colors, organization & layout, the section highlights are nice
We don't like: lack of textures, lack subtle illustrations/icons.

http://www.plateglimpse-example.com/menuwall/archives/wexford_mill.php
We like: use of textures, typefaces, layout & organization, single page menu
We don't like: lack of textures, lack of bold color, lack of icons and menu item hightlights

http://www.plateglimpse-example.com/menuwall/archives/pelino_bis.php
We like: use of texturing, typesfaces, layout & organization, creative use of illustrations/icons, bold colors
We don't like: not a huge fan of the bordering; and illustrations take up too much room for single page menu

http://www.plateglimpse-example.com/menuwall/archives/ved_siden_af_torvet.php
We like: creative use of typefaces, organization & layout, cool illustrations, oversized menu, section seperators are cool & unique
We don't like: lack of textures, menu items inside illustrations, typefaces can get hard to read in certain areas
Should not have
• Do Not Use

• Skeuomorphism in any way.
• We do not want any actual pictures of food on the menu (subtle illustrations / icons are great and encouraged).
• Typefaces that are hard to read.

```html
<!DOCTYPE html>
<html lang="en">
<head>
<meta charset="utf-8">
<title>Lantern Cafe – Breakfast Menu</title>
<link href="https://fonts.googleapis.com/css2?family=Roboto+Slab:wght@800&family=Bungee+Inline&family=Oswald:wght@400;500&family=Cabin:wght@400;600&family=Kalam:wght@700&display=swap" rel="stylesheet">
<style>
  :root {
    --paper: #f6e8d2;
    --red: #ec1f27;
    --red-soft: #f04a50;
    --orange: #f37022;
    --orange-mid: #f78f20;
    --orange-light: #faa54b;
  }
  * { box-sizing: border-box; margin: 0; padding: 0; }
  html, body { width: 1200px; height: 900px; overflow: hidden; background: var(--paper); }
  .menu { position: relative; width: 1200px; height: 900px; background: var(--paper); color: var(--orange); font-family: "Cabin", sans-serif; }
  .abs { position: absolute; white-space: nowrap; }

  .top-band { position: absolute; top: 16px; height: 40px; background: var(--red-soft); opacity: .75; }
  .menu-title { position: absolute; top: 6px; left: 370px; width: 444px; text-align: center; font-family: "Bungee Inline", sans-serif; font-size: 54px; letter-spacing: 8px; color: var(--red-soft); line-height: 1; font-weight: 400; }

  .section-title { font-family: "Roboto Slab", serif; font-weight: 800; color: var(--red); line-height: 1; letter-spacing: .5px; }
  .ribbon { position: absolute; left: 326px; top: 72px; }
  .ribbon-text { position: absolute; left: 350px; top: 81px; width: 200px; text-align: center; font-size: 8px; line-height: 1.3; color: #fff; }

  .builder { font-family: "Oswald", sans-serif; font-weight: 500; color: var(--orange-mid); text-align: center; width: 540px; left: 57px; }
  .builder-tag { font-family: "Kalam", cursive; font-weight: 700; color: var(--orange); font-size: 20px; }

  .item { font-family: "Oswald", sans-serif; font-weight: 500; font-size: 21px; color: var(--orange); line-height: 1; letter-spacing: -.2px; }
  .item .price { margin-left: 40px; }
  .item .note { font-family: "Cabin", sans-serif; font-weight: 400; font-size: 13px; letter-spacing: 0; margin-left: 6px; }
  .item.variant { color: var(--orange-light); }
  .desc { font-size: 14px; color: var(--orange); line-height: 20px; }

  .sides-box { position: absolute; left: 646px; top: 485px; width: 504px; height: 381px; border: 2px solid var(--red); box-shadow: 6px 6px 0 var(--red-soft); background: var(--paper); }
  .sides-rule { position: absolute; left: 661px; top: 556px; width: 474px; height: 4px; background: var(--red-soft); }
  .side { font-weight: 600; font-size: 15px; color: var(--orange); left: 665px; line-height: 1; }
  .side .price { margin-left: 32px; }
  .side.light { color: var(--orange-light); }
  .icon { position: absolute; }
</style>
</head>
<body>
<main class="menu">
  <div class="top-band" style="left:0;width:366px"></div>
  <div class="top-band" style="left:818px;width:382px"></div>
  <h1 class="menu-title">BREAKFAST</h1>

  <!-- Omelets -->
  <h2 class="section-title abs" style="left:68px;top:70px;font-size:44px">OMELETS</h2>
  <svg class="ribbon" width="244" height="42" viewBox="0 0 244 42">
    <polygon points="0,0 20,4 14,26 4,26" fill="var(--red)"/>
    <polygon points="14,6 226,6 218,34 8,34" fill="var(--red)"/>
    <polygon points="216,14 244,14 236,40 212,30" fill="var(--red)"/>
  </svg>
  <p class="ribbon-text">All omelettes come with three farm fresh eggs, toasted homefries, and your choice of toast.</p>

  <svg class="abs" style="left:56px;top:120px" width="50" height="160" viewBox="0 0 50 160">
    <path d="M46 4 C20 4 26 30 24 60 C22 76 14 80 4 80 C14 80 22 84 24 100 C26 130 20 156 46 156" fill="none" stroke="var(--orange-mid)" stroke-width="5"/>
  </svg>
  <svg class="abs" style="left:550px;top:122px" width="50" height="160" viewBox="0 0 50 160">
    <path d="M4 4 C30 4 24 30 26 60 C28 76 36 80 46 80 C36 80 28 84 26 100 C24 130 30 156 4 156" fill="none" stroke="var(--orange-mid)" stroke-width="5"/>
  </svg>
  <p class="abs builder builder-tag" style="top:126px">&lt;build your own&gt;</p>
  <p class="abs builder" style="top:157px;font-size:21px;line-height:27px">MUSHROOMS, TOMATOES, ONION, BROCCOLI, SPINACH,<br>PEPPERS,&nbsp; JALAPENOS &nbsp; /0.50 EACH/</p>
  <div class="abs" style="left:208px;top:216px;width:222px;height:2px;background:var(--orange)"></div>
  <p class="abs builder" style="top:223px;font-size:21px">EGG WHITES &nbsp; /1.50/</p>
  <p class="abs builder builder-tag" style="top:250px">&lt;/build your own&gt;</p>

  <p class="abs item" style="left:68px;top:294px">SOUTH WEST WHITE VEGGIE OMELET<span class="price">10.95</span></p>
  <p class="abs desc" style="left:68px;top:320px">4 egg whites with Monterrey Jack cheese, Tomatoes, Onions, peppers, Spinach and our<br>home made salsa and served with sliced tomatoes</p>
  <p class="abs item" style="left:68px;top:368px">HASTA LA FEASTA<span class="price">7.95</span></p>
  <p class="abs desc" style="left:68px;top:393px">3 Scrambled eggs in tortillas topped with melted cheese and our home made salsa</p>
  <p class="abs item" style="left:68px;top:422px">GRECIAN OMELET<span class="note">/Spinach, Feta/</span><span class="price" style="margin-left:52px">8.95</span></p>
  <p class="abs item" style="left:68px;top:458px">HUNTERS OMELET<span class="note">/Bacon, Potato, Onions, Cheddar/</span><span class="price">8.95</span></p>
  <p class="abs item" style="left:68px;top:494px">FRUITY FRENCH PIG OMELET<span class="note">/Ham, Brie, Raspberry Jam/</span><span class="price">8.95</span></p>
  <p class="abs item" style="left:68px;top:529px">WESTERN OMELET<span class="note">/Ham, Cheddar, Pepper, Onion/</span><span class="price">8.95</span></p>

  <!-- Pancakes -->
  <h2 class="section-title abs" style="left:68px;top:568px;font-size:40px;line-height:43px">PANCAKES &amp;<br>FRENCH TOAST</h2>
  <div class="icon" role="img" aria-label="Small bread slice icon" style="left:424px;top:580px;width:68px;height:60px;background:var(--red-soft);border-radius:18px 18px 6px 6px"></div>

  <p class="abs item" style="left:68px;top:660px">GLUTTON’S PARADISE<span class="price">8.95</span></p>
  <p class="abs desc" style="left:68px;top:686px">3 eggs your way, 2 pancakes and a breakfast side of your choice</p>
  <p class="abs item" style="left:68px;top:720px;color:var(--orange-mid)">BUTTERMILK PANCAKES/3<span class="price">5.25</span></p>
  <p class="abs item" style="left:68px;top:748px;color:var(--orange-mid)">BUTTERMILK PANCAKES/2<span class="price">4.25</span></p>
  <p class="abs item" style="left:68px;top:790px;color:var(--orange-mid)">FRENCH TOAST/4<span class="price">5.50</span></p>
  <p class="abs item" style="left:68px;top:818px;color:var(--orange-mid)">FRENCH TOAST/3<span class="price">4.50</span></p>
  <p class="abs item variant" style="left:68px;top:855px">UPGRADE TO 100% MAPLE SYRUP<span class="price">1.50</span></p>

  <!-- Eggs -->
  <h2 class="section-title abs" style="left:659px;top:72px;font-size:44px">EGGS</h2>
  <div class="icon" role="img" aria-label="Small fried egg icon" style="left:832px;top:66px;width:56px;height:56px;background:var(--red-soft);border-radius:50%"></div>

  <p class="abs item" style="left:659px;top:137px">EGGS, TATERS &amp; TOAST<span class="price">5.50</span></p>
  <p class="abs desc" style="left:659px;top:161px">3 farm fresh eggs, toasted home fries, and choice of toast</p>
  <p class="abs item variant" style="left:659px;top:184px">/WITH EGG WHITES<span class="price">7</span></p>
  <p class="abs item" style="left:659px;top:225px">EGG SANDWICH<span class="price">3.50</span></p>
  <p class="abs desc" style="left:659px;top:250px">2 farm fresh eggs on your choice of toasted bread</p>
  <p class="abs item variant" style="left:659px;top:271px">/WITH CHEESE<span class="price">4</span></p>
  <p class="abs item" style="left:659px;top:308px">DELUXE EGG SANDWICH<span class="price">4.75</span></p>
  <p class="abs desc" style="left:659px;top:333px">Your choice of meat or veggies, cheese, and two farm fresh eggs</p>
  <p class="abs item variant" style="left:659px;top:355px">/IN A BAGEL OR WRAP<span class="price">5.25</span></p>
  <p class="abs item" style="left:659px;top:394px">BREAKFAST BURRITO<span class="price">5.95</span></p>
  <p class="abs desc" style="left:659px;top:419px">Large Flour Tortilla filled with Scrambled Eggs, bacon, black beans,<br>Home fries, cheddar cheese, and our home made salsa</p>

  <!-- Sides -->
  <div class="sides-box"></div>
  <h2 class="section-title abs" style="left:672px;top:503px;font-size:42px">BREAKFAST SIDES</h2>
  <div class="sides-rule"></div>
  <p class="abs side" style="top:576px;line-height:18px">Ridgeline Bacon, Hollowbrook Turkey Bacon, Sausage, Turkey Sausage,<br>Pinecrest Pork Roll or Ham Slice<span class="price">2.75</span></p>
  <p class="abs side" style="top:620px">Side of Home fries<span class="price">2</span></p>
  <p class="abs side" style="top:646px">Side of Eggs<span class="price">2.50</span></p>
  <p class="abs side" style="top:672px">Big English Muffin<span class="price">1.25</span></p>
  <p class="abs side" style="top:698px">Toast<span class="price">1.25</span></p>
  <p class="abs side" style="top:725px">Grilled Yogurt Muffin<span class="price">1.75</span></p>
  <p class="abs side" style="top:751px">Toasted Bagel<span class="price">1.50</span><span style="margin-left:20px;color:var(--orange-light)">/with cream cheese</span><span class="price">2</span></p>
  <p class="abs side" style="top:778px">Hearthstone Oatmeal with brown sugar and milk<span class="price">3</span></p>
  <p class="abs side light" style="top:804px">/with raisins<span class="price">3.50</span><span style="margin-left:20px">/with fruit</span><span class="price">4.50</span></p>
  <p class="abs side" style="top:831px">Quinoa with raisins and fruit<span class="price">5</span></p>
</main>
</body>
</html>
```